December online webinar for our coaching and mentoring business.

needing an email flyer and something to use on appropriate social media e.g. Instagram to promote our December half day webinar focusing on positive mindset, relationships and 2021 being a new year with new opportunities. For the feel of what we have done previously:
www.qlvgetaways.com.au
We will be using 2 guest speakers:
Marcus Elwood of BucketGoals.com and
Lorena Voss, psychologist and both will need to be prominent on the marketing material we send out on email and use on social media.
The webinar will likely run Thursday December 10th from 12.30pm to 4.30pm AEST and will be hosted and facilitated by me and on behalf of Tarrow Business Coaching.
I am thinking colour schemes and branding similar to what you see on the website above.
Pricing needs to be on the flyer - $750 + GST per person*
*enquire for multi booking discounts for 2 people or more

Target Market(s)

people looking for a boost before the year end and a fast start to 2021

Font styles to use
Sans Serif

Requirements
Must have
• see brief above
Nice to have
• see brief above
Should not have
• see brief above

```html
<!DOCTYPE html>
<html lang="en">
<head>
<meta charset="utf-8">
<title>Positive Mindset, Relationships and 2021 – Webinar</title>
<link href="https://fonts.googleapis.com/css2?family=Montserrat:wght@600;700&family=Oswald:wght@400;500&family=Open+Sans:wght@400;600&display=swap" rel="stylesheet">
<style>
  :root{
    --brand-red:#e8473a;
    --deep-red:#e23c2f;
    --ink:#2b2b2b;
    --body-text:#444;
    --hero-dark:#2d3136;
    --hero-mid:#6b7177;
    --white:#ffffff;
    --photo-grey:#6e6e6e;
    --silhouette:#1d1d1d;
  }
  *{margin:0;padding:0;box-sizing:border-box}
  html,body{width:706px;height:1200px;overflow:hidden;background:var(--white)}
  body{font-family:"Open Sans",Arial,sans-serif;color:var(--body-text)}
  .flyer{position:relative;width:706px;height:1200px;background:var(--white)}

  .hero{position:absolute;left:0;top:0;width:706px;height:450px;
    background:linear-gradient(115deg,var(--hero-dark) 0%,#464b51 45%,var(--hero-mid) 75%,#9ca1a5 100%)}
  .brand{position:absolute;left:26px;top:22px;display:flex;align-items:center;gap:10px}
  .brand-mark{width:14px;height:14px;background:var(--deep-red)}
  .brand-name{font-family:"Montserrat",Arial,sans-serif;font-weight:700;font-size:22px;color:var(--deep-red);letter-spacing:.3px}
  .hero-title{position:absolute;left:28px;top:232px;width:520px;
    font-family:"Montserrat",Arial,sans-serif;font-weight:700;font-size:40px;line-height:46px;color:var(--white)}
  .tagline{position:absolute;left:0;top:368px;width:412px;height:82px;background:var(--brand-red);
    padding:12px 0 0 28px;font-family:"Oswald",Arial,sans-serif;font-weight:500;font-size:24px;line-height:29px;color:var(--white);letter-spacing:.5px}

  .speakers-heading{position:absolute;left:28px;top:470px;font-family:"Oswald",Arial,sans-serif;font-weight:500;
    font-size:34px;color:var(--brand-red);letter-spacing:.5px}
  .speaker{position:absolute;left:28px;width:650px}
  .speaker-one{top:530px}
  .speaker-two{top:736px}
  .speaker-photo{position:absolute;left:0;top:0;width:148px;height:176px}
  .speaker-one .speaker-photo{background:linear-gradient(160deg,#9a9a9a,var(--photo-grey) 55%,#2e2e2e)}
  .speaker-two .speaker-photo{background:linear-gradient(180deg,#f4f4f4,#d9d9d9)}
  .speaker-info{position:absolute;left:195px;top:0;width:455px}
  .speaker-name{font-family:"Oswald",Arial,sans-serif;font-weight:500;font-size:22px;color:var(--ink);letter-spacing:.5px;margin-bottom:10px}
  .speaker-info p{font-size:12.2px;line-height:17px;margin-bottom:13px}

  .event-box{position:absolute;left:28px;top:1000px;width:650px;height:188px;background:var(--brand-red);
    text-align:center;color:var(--white);padding-top:22px}
  .event-date{font-family:"Oswald",Arial,sans-serif;font-weight:500;font-size:33px;letter-spacing:.5px;margin-bottom:22px}
  .event-price{font-family:"Oswald",Arial,sans-serif;font-weight:400;font-size:21px;line-height:30px;letter-spacing:.4px}
</style>
</head>
<body>
<div class="flyer">
  <header class="hero" role="img" aria-label="Photo of a laptop showing a presenter pointing at a screen, dark grey tones">
    <div class="brand"><span class="brand-mark"></span><span class="brand-name">Tarrow Business Coaching</span></div>
    <h1 class="hero-title">Positive Mindset, Relationships and 2021</h1>
    <div class="tagline">BEING A NEW YEAR<br>WITH NEW OPPORTUNITIES</div>
  </header>

  <h2 class="speakers-heading">GUEST SPEAKERS</h2>

  <section class="speaker speaker-one">
    <div class="speaker-photo" role="img" aria-label="Black and white portrait photo of guest speaker Marcus Elwood"></div>
    <div class="speaker-info">
      <h3 class="speaker-name">MARCUS ELWOOD</h3>
      <p>After the loss of a close friend in his early twenties, he penned down a list of 100 goals that he hoped would bring him closer to a sense of happiness.</p>
      <p>Now 10 years on and counting, Marcus has ticked off 74 items from his list, has raised almost half a million dollars for charities and has found a sense of purpose that he could never have dreamt of.</p>
      <p>His story turned into books, TV shows and documentaries, has most impressively inspired a global community of individuals and organizations who have identified, pursued, and achieved their own goals, too.</p>
    </div>
  </section>

  <section class="speaker speaker-two">
    <div class="speaker-photo" role="img" aria-label="Placeholder silhouette portrait for guest speaker Lorena Voss"></div>
    <div class="speaker-info">
      <h3 class="speaker-name">LORENA VOSS</h3>
      <p>Lorem ipsum dolor sit amet, consectetur adipiscing elit, sed do eiusmod tempor incididunt ut labore et dolore magna aliqua. Ut enim ad minim veniam, quis nostrud exercitation</p>
      <p>ullamco laboris nisi ut aliquip ex ea commodo consequat. Duis aute irure dolor in reprehenderit in voluptate velit esse cillum dolore eu fugiat nulla pariatur. Excepteur sint occaecat cupidatat non proident, sunt in culpa qui officia deserunt mollit anim id est laborum.</p>
    </div>
  </section>

  <section class="event-box">
    <div class="event-date">DECEMBER 10TH FROM 12.30PM TO 4.30PM AEST</div>
    <div class="event-price">$750 + GST PER PERSON*<br>*ENQUIRE FOR MULTI BOOKING DISCOUNTS FOR 2 PEOPLE OR MORE</div>
  </section>
</div>
</body>
</html>
```